Content company in need of a single PowerPoint slide

The goal of this slide is to visually convey that Product A does a far superior job of creating and organizing content to find your answer than the competitor's Product B. Product A not only has more content, it also has a much more granular organization of that content which makes it easier to find your answer.

Story:

1) A user would like to find the answer to a specific issue that he/she is researching.

2) Both Product A and Product B start with the same General Document on the topic. But this General Document itself doesn't actually have the specific answer to the user's issue.

3) At this point the user needs to browse to related content to find their answer.

4) Product A provides the user with 400 related documents specifically related to that #1 document. The 400 related documents are organized into discrete categories and sub-categories (child categories), such that within each sub-category there are a small number of documents on a specific issue.
a) There may be 10-30 categories, with 3-5 sub-categories in each category (total 90 categories and sub-categories)
b) The categories are organized alphabetically.

5) Product B provides the user with only 250 related documents which are also categorized.
a) Product B also has only has one-third (1/3) the number of categorizes and sub-categories of Product A. So a total of 30 categories and sub-categories.

6) Product A contains a category that relates to the user’s issue, and then a more specific sub-category which provides 11 closely related documents. Thus the user is able to quickly identify the 11 of the 400 related documents relevant to the issue they are researching, when starting with the General Document.

7) Product B has no categories specifically addressing the issue they are researching. Thus the user must manually navigate through all categories to see if any of the 250 related documents address the issue which may take a long time.

Presentation to audience:

The slide must visually convey the point to the audience with limited use of text.

File specifics:

Preferably this design will be done in Photoshop and then exported as PNG to be placed inside a PPT (7x5 = 1024px x 768px).

Provide PSD file only.

Requirements
Must have
• Visual recognition that Product A has more content that is categorized more comprehensively than Product B.
Nice to have
• Content can be visualized using document icons.

```html
<!DOCTYPE html>
<html lang="en">
<head>
<meta charset="utf-8">
<title>Product A vs Product B – Finding Your Answer</title>
<link rel="stylesheet" href="https://fonts.googleapis.com/css2?family=Montserrat:wght@500;800&family=Nunito:wght@800;900&display=swap">
<style>
  :root {
    --blue-top: #38b8f2;
    --blue-mid: #1f8ad6;
    --blue-deep: #155fae;
    --grey-bg: #f3f3f3;
    --grey-ink: #575757;
    --grey-dash: #6a6a6a;
    --white: #ffffff;
    --panel: #3a3d42;
    --doc-blue: #1f7fc4;
    --icon-blue: #9fd4f5;
    --green: #7cc242;
    --orange: #f7941d;
    --sky: #29abe2;
    --yellow: #ffe600;
    --check: #8a8c90;
  }
  * { box-sizing: border-box; margin: 0; padding: 0; }
  html, body { width: 1200px; height: 900px; overflow: hidden; }
  body { font-family: "Nunito", Arial, sans-serif; }
  .slide { position: relative; width: 1200px; height: 900px; overflow: hidden; background: var(--grey-bg); }
  .side-a {
    position: absolute; left: 0; top: 0; width: 598px; height: 900px;
    background: linear-gradient(180deg, var(--blue-top) 0%, var(--blue-mid) 55%, var(--blue-deep) 100%);
  }
  .answer-panel { position: absolute; left: 0; top: 703px; width: 598px; height: 131px; background: var(--panel); }
  .diagram { position: absolute; left: 0; top: 0; }
  .product-title {
    position: absolute; top: 20px; font-family: "Montserrat", sans-serif; font-weight: 500;
    font-size: 40px; letter-spacing: 1px; line-height: 1;
  }
  .product-title b { font-weight: 800; font-size: 44px; }
  .product-title.a { left: 33px; color: var(--white); }
  .product-title.b { right: 34px; color: var(--grey-ink); }
  .search-box {
    position: absolute; left: 398px; top: 23px; width: 419px; height: 36px;
    background: var(--white); border: 1px solid #cfd6dc; border-radius: 3px;
    font-family: "Montserrat", sans-serif; font-size: 16px; color: #6b6b6b;
    padding: 8px 12px; line-height: 18px;
  }
  .search-btn {
    position: absolute; right: 4px; top: 4px; width: 28px; height: 26px;
    border: 1px solid #c4c4c4; border-radius: 3px; background: #f6f6f6;
  }
  .stat { position: absolute; font-weight: 900; line-height: 1; white-space: nowrap; }
  .stat .num { font-size: 60px; letter-spacing: -1px; }
  .stat .label { font-size: 32px; font-weight: 800; }
  .stat.a { color: var(--white); }
  .stat.b { color: var(--grey-ink); }
  .stat.mid .num { font-size: 40px; }
  .stat.mid .label { font-size: 23px; }
  .stat-related-a { left: 115px; top: 222px; }
  .stat-related-b { left: 633px; top: 222px; }
  .stat-cat-a { left: 113px; top: 362px; }
  .stat-cat-b { left: 637px; top: 364px; }
  .closely { position: absolute; left: 201px; top: 458px; color: var(--white); display: flex; align-items: flex-start; gap: 6px; }
  .closely .num { font-size: 40px; font-weight: 900; line-height: 1; }
  .closely .label { font-size: 21px; font-weight: 800; line-height: 1.2; text-align: right; padding-top: 4px; }
  .no-sub { position: absolute; left: 708px; top: 470px; color: var(--grey-ink); font-size: 19px; font-weight: 800; line-height: 1.35; }
  .your-answer { position: absolute; left: 382px; top: 800px; color: var(--white); font-size: 20px; font-weight: 900; }
</style>
</head>
<body>
<div class="slide">
  <div class="side-a"></div>
  <div class="answer-panel"></div>

  <svg class="diagram" width="1200" height="900" viewBox="0 0 1200 900" aria-hidden="true">
    <defs>
      <marker id="arrow-white" markerWidth="8" markerHeight="8" refX="6" refY="4" orient="auto" markerUnits="userSpaceOnUse">
        <path d="M0,0 L8,4 L0,8 Z" fill="#fff"/>
      </marker>
      <marker id="arrow-grey" markerWidth="8" markerHeight="8" refX="6" refY="4" orient="auto" markerUnits="userSpaceOnUse">
        <path d="M0,0 L8,4 L0,8 Z" fill="#6a6a6a"/>
      </marker>
      <symbol id="doc-pair" viewBox="0 0 32 32">
        <path d="M9 1 H22 L29 8 V27 H9 Z" fill="currentColor" opacity="0.85"/>
        <path d="M3 5 H16 L23 12 V31 H3 Z" fill="currentColor" stroke="var(--stroke,none)" stroke-width="1.5"/>
        <path d="M16 5 V12 H23" fill="none" stroke="var(--stroke,#fff)" stroke-width="1.5"/>
      </symbol>
      <symbol id="doc-outline" viewBox="0 0 38 46">
        <path d="M2 2 H26 L36 12 V44 H2 Z M26 2 V12 H36" fill="none" stroke="currentColor" stroke-width="3" stroke-linejoin="round"/>
      </symbol>
    </defs>

    <!-- search magnifier -->
    <g transform="translate(789 29)" stroke="#555" stroke-width="2" fill="none">
      <circle cx="14" cy="10" r="5"/><line x1="10" y1="14" x2="5" y2="19"/>
    </g>

    <!-- general document card -->
    <rect x="535" y="73" width="122" height="129" fill="#fff"/>
    <path d="M555 88 H610 L640 118 V188 H555 Z" fill="var(--doc-blue)"/>
    <path d="M610 92 L636 118 H610 Z" fill="#fff"/>

    <!-- connectors product A -->
    <g stroke="#fff" stroke-width="2" stroke-dasharray="5 5" fill="none">
      <path d="M512 131 H59 V190" marker-end="url(#arrow-white)"/>
      <path d="M64 288 V381 H106" marker-end="url(#arrow-white)"/>
      <path d="M141 398 V483 H183" marker-end="url(#arrow-white)"/>
      <path d="M228 520 V566"/>
    </g>
    <circle cx="512" cy="131" r="5" fill="#fff"/>

    <!-- connectors product B -->
    <g stroke="var(--grey-dash)" stroke-width="2" stroke-dasharray="5 5" fill="none">
      <path d="M674 131 H1127 V192" marker-end="url(#arrow-grey)"/>
      <path d="M1137 292 V382 H1100" marker-end="url(#arrow-grey)"/>
      <path d="M1108 402 V494 H1075" marker-end="url(#arrow-grey)"/>
      <path d="M1058 516 V566"/>
    </g>
    <circle cx="674" cy="131" r="5" fill="var(--grey-dash)"/>

    <!-- big related-doc icons -->
    <g transform="translate(40 212)" style="color:#fff;--stroke:var(--blue-mid)"><use href="#doc-pair" width="66" height="66"/></g>
    <g transform="translate(1088 213)" style="color:var(--grey-ink);--stroke:var(--grey-bg)"><use href="#doc-pair" width="66" height="66"/></g>

    <!-- clock -->
    <g transform="translate(663 493)">
      <circle r="28" fill="#fff" stroke="var(--grey-ink)" stroke-width="3"/>
      <g stroke="var(--grey-ink)" stroke-width="2">
        <line x1="0" y1="-24" x2="0" y2="-19"/><line x1="0" y1="19" x2="0" y2="24"/>
        <line x1="-24" y1="0" x2="-19" y2="0"/><line x1="19" y1="0" x2="24" y2="0"/>
      </g>
      <path d="M0 2 L0 -18 M0 2 L-8 12" stroke="var(--grey-ink)" stroke-width="3" stroke-linecap="round"/>
    </g>

    <!-- tree A -->
    <g stroke="#fff" stroke-width="2" fill="none">
      <line x1="57" y1="570" x2="548" y2="570"/>
      <path d="M57 570 V590 M176 570 V590 M231 570 V590 M281 570 V590 M334 570 V590 M387 570 V590 M436 570 V590 M490 570 V590 M548 570 V590"/>
      <path d="M127 570 V586"/>
    </g>
    <path d="M121 584 L133 584 L127 594 Z" fill="#fff"/>

    <!-- tree B -->
    <g stroke="var(--grey-ink)" stroke-width="2" fill="none">
      <line x1="652" y1="570" x2="1148" y2="570"/>
      <path d="M652 570 V592 M723 570 V592 M775 570 V592 M827 570 V592 M880 570 V592 M933 570 V592 M986 570 V592 M1039 570 V592 M1094 570 V592 M1148 570 V592"/>
    </g>

    <!-- doc row A -->
    <g style="color:var(--icon-blue);--stroke:var(--blue-mid)" font-family="Nunito, sans-serif" font-weight="900" font-size="13" fill="#fff">
      <use href="#doc-pair" x="44" y="624" width="34" height="34"/>
      <use href="#doc-pair" x="162" y="624" width="34" height="34"/>
      <use href="#doc-pair" x="216" y="624" width="34" height="34"/>
      <use href="#doc-pair" x="268" y="624" width="34" height="34"/>
      <use href="#doc-pair" x="320" y="624" width="34" height="34"/>
      <use href="#doc-pair" x="373" y="624" width="34" height="34"/>
      <use href="#doc-pair" x="422" y="624" width="34" height="34"/>
      <use href="#doc-pair" x="476" y="624" width="34" height="34"/>
      <use href="#doc-pair" x="531" y="624" width="34" height="34"/>
    </g>
    <g font-family="Nunito, sans-serif" font-weight="900" font-size="13" fill="var(--blue-mid)">
      <rect x="44" y="641" width="16" height="17" fill="var(--icon-blue)"/><text x="47" y="655">A</text>
      <rect x="162" y="641" width="16" height="17" fill="var(--icon-blue)"/><text x="165" y="655">C</text>
      <rect x="216" y="641" width="16" height="17" fill="var(--icon-blue)"/><text x="219" y="655">D</text>
      <rect x="268" y="641" width="16" height="17" fill="var(--icon-blue)"/><text x="271" y="655">E</text>
      <rect x="320" y="641" width="16" height="17" fill="var(--icon-blue)"/><text x="323" y="655">F</text>
      <rect x="373" y="641" width="16" height="17" fill="var(--icon-blue)"/><text x="375" y="655">G</text>
      <rect x="422" y="641" width="16" height="17" fill="var(--icon-blue)"/><text x="425" y="655">H</text>
      <rect x="476" y="641" width="16" height="17" fill="var(--icon-blue)"/><text x="481" y="655">I</text>
      <rect x="531" y="641" width="16" height="17" fill="var(--icon-blue)"/><text x="535" y="655">J</text>
    </g>
    <g style="color:var(--green);--stroke:#4c8d1e"><use href="#doc-pair" x="92" y="600" width="60" height="60"/></g>

    <!-- doc row B -->
    <g style="color:var(--grey-ink);--stroke:var(--grey-bg)">
      <use href="#doc-pair" x="643" y="624" width="34" height="34"/>
      <use href="#doc-pair" x="698" y="624" width="34" height="34"/>
      <use href="#doc-pair" x="762" y="624" width="34" height="34"/>
      <use href="#doc-pair" x="815" y="624" width="34" height="34"/>
      <use href="#doc-pair" x="868" y="624" width="34" height="34"/>
      <use href="#doc-pair" x="921" y="624" width="34" height="34"/>
      <use href="#doc-pair" x="973" y="624" width="34" height="34"/>
      <use href="#doc-pair" x="1024" y="624" width="34" height="34"/>
      <use href="#doc-pair" x="1076" y="624" width="34" height="34"/>
      <use href="#doc-pair" x="1128" y="624" width="34" height="34"/>
    </g>
    <g font-family="Nunito, sans-serif" font-weight="900" font-size="13" fill="#fff">
      <text x="646" y="655">A</text><text x="701" y="655">B</text><text x="765" y="655">C</text>
      <text x="818" y="655">D</text><text x="871" y="655">E</text><text x="924" y="655">F</text>
      <text x="975" y="655">G</text><text x="1026" y="655">H</text><text x="1082" y="655">I</text>
      <text x="1132" y="655">J</text>
    </g>

    <!-- answer panel pointer -->
    <path d="M100 704 L114 674 L128 704 Z" fill="var(--panel)"/>

    <!-- eleven closely related docs -->
    <use href="#doc-outline" x="30" y="742" width="38" height="46" style="color:var(--green)"/>
    <use href="#doc-outline" x="82" y="742" width="38" height="46" style="color:var(--green)"/>
    <use href="#doc-outline" x="133" y="742" width="38" height="46" style="color:var(--green)"/>
    <use href="#doc-outline" x="183" y="742" width="38" height="46" style="color:var(--orange)"/>
    <use href="#doc-outline" x="233" y="742" width="38" height="46" style="color:var(--orange)"/>
    <use href="#doc-outline" x="283" y="742" width="38" height="46" style="color:var(--orange)"/>
    <use href="#doc-outline" x="333" y="742" width="38" height="46" style="color:var(--sky)"/>
    <use href="#doc-outline" x="382" y="742" width="38" height="46" style="color:var(--sky)"/>
    <use href="#doc-outline" x="432" y="742" width="38" height="46" style="color:var(--check)"/>
    <path d="M440 760 L450 772 L466 748" fill="none" stroke="#fff" stroke-width="5" stroke-linecap="round" stroke-linejoin="round"/>
    <use href="#doc-outline" x="483" y="742" width="38" height="46" style="color:var(--yellow)"/>
    <use href="#doc-outline" x="532" y="742" width="38" height="46" style="color:var(--yellow)"/>
  </svg>

  <div class="product-title a">PRODUCT <b>A</b></div>
  <div class="product-title b">PRODUCT <b>B</b></div>
  <div class="search-box">I need an answer to a specific issue…<span class="search-btn"></span></div>

  <div class="stat a stat-related-a"><span class="num">400</span> <span class="label">Related Documents</span></div>
  <div class="stat b stat-related-b" style="left:633px"><span class="num">250</span> <span class="label">Related Documents</span></div>

  <div class="stat a mid stat-cat-a"><span class="num">90</span> <span class="label">Categories and Sub-Categories</span></div>
  <div class="stat b mid stat-cat-b"><span class="num">30</span> <span class="label">Categories and Sub-Categories</span></div>

  <div class="closely"><span class="num">11</span><span class="label">Closely Related Documents<br>in Specific Sub-Category</span></div>
  <div class="no-sub">There is no Specific Sub-Category<br>Manually navigate all 250 files</div>

  <div class="your-answer">Your Answer</div>
</div>
</body>
</html>
```